Pelkman Agency (http://pa.quorvexstudio.com/)

We are looking for a similar design to what we have, but more professional looking and cleaned up with links and logo that is not so grainy looking. We are an independent insurance agency marketing to personal and commercial clients. We offer all commercial lines markets and all personal lines. We target excavators, landscapers, restaurants, golf courses, contractors. Please look at http://pa.quorvexstudio.com/ which we had designed but do not like it, it will give you an idea of what we are looking for.

Target Market(s)

Commercial and personal insurance. All business products and all personal (homeowners, auto, antique auto, umbrella)

Industry/Entity Type

It Professional

Logo Text

Knowledge Building Your Assurance

Number of Pages Required

5+ page

Colors
000000
848484
0255a3

```html
<!DOCTYPE html>
<html lang="en">
<head>
<meta charset="utf-8">
<title>Pelkman Agency</title>
<link href="https://fonts.googleapis.com/css2?family=Open+Sans:wght@400;600;700&family=Oswald:wght@500&display=swap" rel="stylesheet">
<style>
:root{
  --blue:#0255a3;
  --black:#000000;
  --grey:#848484;
  --dark:#2b2b2b;
  --darker:#1c1c1c;
  --lime:#9cc21f;
  --light:#f2f2f2;
  --line:#dcdcdc;
  --text:#555555;
}
*{box-sizing:border-box;margin:0;padding:0}
html,body{width:736px;height:1200px;overflow:hidden;background:#fff;font-family:"Open Sans",Arial,sans-serif;color:var(--text)}
.page{width:736px;height:1200px;position:relative}
.wrap{width:680px;margin:0 auto;position:relative}

/* header */
.header{height:72px}
.header .wrap{height:72px;display:flex;align-items:center;justify-content:space-between}
.brand{display:flex;align-items:center;gap:8px}
.brand-mark{width:30px;height:30px;background:var(--blue)}
.brand-name{font-weight:700;font-size:24px;color:var(--blue);letter-spacing:1px}
.header-right{display:flex;flex-direction:column;align-items:flex-end;gap:8px}
.contact-line{font-size:8px;color:var(--grey);display:flex;gap:14px}
.social{display:flex;gap:5px}
.social span{width:16px;height:16px;background:var(--grey);border-radius:2px}

/* nav */
.nav{height:26px;background:var(--dark)}
.nav .wrap{display:flex;height:26px;align-items:center}
.nav a{font-size:8px;font-weight:600;color:#fff;text-decoration:none;padding:0 12px;height:26px;line-height:26px;white-space:nowrap}
.nav a.active{background:var(--blue)}
.nav .search{margin-left:auto;display:flex}
.nav .search i{width:110px;height:16px;background:#fff;display:block}
.nav .search b{width:18px;height:16px;background:var(--lime);display:block}

/* hero */
.hero{height:196px;background:linear-gradient(180deg,#8fc6ec 0%,#cfe8f8 60%,#eef7fd 100%)}
.promo{height:28px;background:var(--lime)}
.promo .wrap{height:28px;display:flex;align-items:center;justify-content:center;gap:12px}
.promo p{font-size:8px;font-weight:600;color:#fff}
.promo .btn{background:var(--dark);color:#fff;font-size:7px;padding:4px 10px}

.intro{text-align:center;font-size:8px;color:var(--text);margin:14px 0 12px}

/* services */
.services{display:flex;justify-content:space-between}
.service{width:158px;text-align:center}
.service .photo{height:98px}
.service h3{font-size:7px;font-weight:600;color:var(--text);margin-top:6px}

/* content */
.content{display:flex;justify-content:space-between;margin-top:18px}
.copy{width:300px}
.copy h2{font-size:16px;color:var(--blue);text-align:center;font-weight:600;margin-bottom:8px}
.copy p{font-size:8px;line-height:1.6;margin-bottom:8px}
.copy .btn{display:inline-block;background:var(--dark);color:#fff;font-size:7px;padding:6px 12px;margin-top:6px}
.video{width:350px;height:200px;position:relative;background:linear-gradient(135deg,#c9c9c9,#ededed 60%,#bfbfbf)}
.video .banner{position:absolute;top:24px;right:16px;background:#6b1d1d;color:#fff;font-family:"Oswald",sans-serif;font-size:24px;padding:4px 14px;letter-spacing:1px}
.video .play{position:absolute;left:155px;top:80px}

/* testimonials */
.lower{display:flex;justify-content:space-between;margin-top:40px}
.section-title{font-size:13px;color:var(--dark);border-bottom:1px solid var(--line);padding-bottom:4px;margin-bottom:8px}
.testimonials{width:440px}
.quote{border:1px solid var(--line);padding:10px 12px;display:flex;gap:10px}
.avatar{width:28px;height:28px;border-radius:50%;background:#c8c8c8;flex:none}
.quote p{font-size:7px;line-height:1.6}
.author{font-size:7px;color:var(--grey);margin-top:6px}
.support{width:210px}
.agents{display:flex;gap:6px}
.agent{flex:1;border:1px solid var(--line);padding:6px;display:flex;gap:5px;align-items:center;font-size:6px}
.agent i{width:14px;height:14px;border-radius:50%;background:var(--lime);flex:none}
.subscribe{display:flex;margin-top:8px}
.subscribe span{flex:1;border:1px solid var(--line);font-size:6px;padding:5px;color:#aaa}
.subscribe b{background:var(--blue);color:#fff;font-size:6px;padding:5px 8px;font-weight:600}

/* partners */
.partners{position:absolute;top:880px;left:0;width:736px;height:100px;background:var(--light);text-align:center;padding-top:18px}
.partners h2{font-size:13px;font-weight:700;color:var(--dark);letter-spacing:.5px}
.partner-row{display:flex;justify-content:center;align-items:center;gap:40px;margin-top:16px}
.partner-row span{width:70px;height:22px;background:#b5b5b5;border-radius:3px}
.partner-row span.round{width:24px;height:24px;border-radius:50%}

/* footer */
.footer{position:absolute;top:980px;left:0;width:736px;height:198px;background:var(--dark);color:#bbb}
.footer .wrap{display:flex;justify-content:space-between;padding-top:14px}
.col{width:158px}
.col h4{font-size:9px;color:#fff;font-weight:600;border-bottom:1px solid #444;padding-bottom:5px;margin-bottom:8px}
.col p,.col li{font-size:6.5px;line-height:1.7}
.col ul{list-style:none}
.col li{border-bottom:1px solid #3a3a3a;padding:2px 0}
.thumbs{display:grid;grid-template-columns:repeat(4,32px);gap:4px}
.thumbs span{height:28px;background:#6f7b86}
.fsocial{display:flex;gap:4px;margin-top:10px}
.fsocial span{width:14px;height:14px;background:#555}
.bottom{position:absolute;top:1178px;left:0;width:736px;height:22px;background:var(--darker);font-size:6.5px;color:#999}
.bottom .wrap{line-height:22px}
</style>
</head>
<body>
<div class="page">
  <header class="header">
    <div class="wrap">
      <div class="brand"><span class="brand-mark"></span><span class="brand-name">PELKMAN</span></div>
      <div class="header-right">
        <div class="contact-line"><span>+1 (555) 014-2290</span><span>info@pelkmanagency.com</span></div>
        <div class="social"><span></span><span></span><span></span><span></span><span></span></div>
      </div>
    </div>
  </header>
  <nav class="nav">
    <div class="wrap">
      <a class="active">HOME</a><a>PERSONAL INSURANCE ▾</a><a>BUSINESS INSURANCE ▾</a><a>SERVICE CENTER ▾</a><a>ABOUT US ▾</a><a>CONTACT US</a>
      <div class="search"><i></i><b></b></div>
    </div>
  </nav>
  <div class="hero" role="img" aria-label="Father lifting child against a blue sky, hand writing insurance words"></div>
  <div class="promo"><div class="wrap"><p>SMALL CIRCLES OF CARE, WE PROTECT WHAT MATTERS MOST</p><span class="btn">Read More</span></div></div>

  <div class="wrap">
    <p class="intro">PLEASE FIND INFORMATION ABOUT OUR AGENCY, ITS PRINCIPLES, AND THE VARIOUS TYPES OF INSURANCE COMPANIES THAT WE PROVIDE.</p>
    <div class="services">
      <div class="service"><div class="photo" role="img" aria-label="Business handshake" style="background:linear-gradient(135deg,#3c5f8a,#9ab4cf)"></div><h3>BUSINESS INSURANCE</h3></div>
      <div class="service"><div class="photo" role="img" aria-label="Family walking outdoors" style="background:linear-gradient(180deg,#8cc3e8,#d9c9a8)"></div><h3>LIFE INSURANCE</h3></div>
      <div class="service"><div class="photo" role="img" aria-label="Hands holding a small car" style="background:linear-gradient(135deg,#e9d7c6,#c85a3a)"></div><h3>AUTO INSURANCE</h3></div>
      <div class="service"><div class="photo" role="img" aria-label="Model house on green lawn" style="background:linear-gradient(180deg,#7fc0e6,#7cbf4a)"></div><h3>HOME INSURANCE</h3></div>
    </div>

    <div class="content">
      <div class="copy">
        <h2>Website Content Goes Here</h2>
        <p>Welcome. Our independent agency offers a full range of personal and commercial coverage from trusted carriers. We work with excavators, landscapers, restaurants, golf courses and contractors to build plans that fit each risk and budget, backed by local service and quick claims help.</p>
        <p>Now, learn more about us and let us review your current policies to find savings and better protection for your family and business.</p>
        <span class="btn">Get More Details</span>
      </div>
      <div class="video" role="img" aria-label="Video still of an advisor presenting long-term care">
        <div class="banner">LONG-TERM CARE</div>
        <svg class="play" width="40" height="40" viewBox="0 0 40 40"><circle cx="20" cy="20" r="19" fill="rgba(0,0,0,.55)" stroke="#fff" stroke-width="2"/><polygon points="16,12 16,28 29,20" fill="#fff"/></svg>
      </div>
    </div>

    <div class="lower">
      <div class="testimonials">
        <h3 class="section-title">Testimonials</h3>
        <div class="quote">
          <span class="avatar"></span>
          <div>
            <p>"Pelkman understood all of our needs from day one. They reviewed our coverage, explained every option clearly and found us a better policy at a lower cost. Friendly, fast and always there when we call."</p>
            <p class="author">Julia Renn · Customer</p>
          </div>
        </div>
      </div>
      <div class="support">
        <h3 class="section-title">Support</h3>
        <div class="agents">
          <div class="agent"><i></i>24/7 ONLINE SUPPORT</div>
          <div class="agent"><i></i>CLAIMS &amp; SERVICE</div>
        </div>
        <div class="subscribe"><span>Your email address</span><b>SUBSCRIBE</b></div>
      </div>
    </div>
  </div>

  <section class="partners">
    <h2>LOTS OF COMPANIES AS OUR PARTNERS</h2>
    <div class="partner-row"><span></span><span></span><span class="round"></span><span class="round"></span><span></span><span></span></div>
  </section>

  <footer class="footer">
    <div class="wrap">
      <div class="col">
        <h4>About Us</h4>
        <p>Pelkman Agency is an independent agency serving personal and commercial clients with trusted carriers and local, friendly service.</p>
        <div class="fsocial"><span></span><span></span><span></span><span></span><span></span></div>
      </div>
      <div class="col">
        <h4>Photostream</h4>
        <div class="thumbs"><span></span><span></span><span></span><span></span><span></span><span></span><span></span><span></span></div>
      </div>
      <div class="col">
        <h4>Recent Posts</h4>
        <ul>
          <li>Protect Your Home This Winter</li>
          <li>Coverage Tips For Contractors</li>
          <li>Is Your Auto Policy Up To Date</li>
          <li>Umbrella Plans Explained</li>
          <li>What To Do After A Claim</li>
        </ul>
      </div>
      <div class="col">
        <h4>Get in Touch</h4>
        <p>118 Harlow Street, Suite 4, Brenton, PA 19020</p>
        <p>Phone: +1 (555) 014-2290</p>
        <p>Email: info@pelkmanagency.com</p>
        <p>Monday–Friday: 9:00am – 5:00pm</p>
        <p>Saturday: 9:00am – 12:00pm</p>
      </div>
    </div>
  </footer>
  <div class="bottom"><div class="wrap">© 2024 Pelkman Agency. All rights reserved.</div></div>
</div>
</body>
</html>
```